New one page Homepage with registration and log in form

Hi designers!

We need a new homepage and made a skitch of how it should be.

Can you give some of your design ideas and work it out so that it actually looks great?

Its just one page, for convertion reasons.

The logo doesnt have to be changed.

It would be cool to center the logo but not sure how design technically correct that is.

The social icons can be left out.

If you could give a few mockups than we can choose the best one.

I added one screenshot sketch of the homepage.

And 2 screenshots of what the system looks like on the inside, just so you get an idea.

Thanks

Target Market(s)

Vacation rental owners who want to increase their bookings by connecting with other VR owners and managers, or by having their own booking team for a small fee.

Industry/Entity Type

Social

Number of Pages Required

1 page

Requirements
Must have
• Use your imagination please
Nice to have
• Use your imagination
• It will be a one page design so we need to impress :)
• Keep it compact, maybe a web 3.0 flat design, etc
Should not have
• Other pages.

```html
<!DOCTYPE html>
<html lang="en">
<head>
<meta charset="utf-8">
<title>Nestwise – The First Social Booking Network</title>
<link href="https://fonts.googleapis.com/css2?family=Open+Sans:wght@400;600;700&family=Noticia+Text&display=swap" rel="stylesheet">
<style>
  :root {
    --page-bg: #fbfbfb;
    --header-bg: #ffffff;
    --line: #d6d6d6;
    --side-bg: #ececec;
    --ink-soft: #7a7a7a;
    --ink-body: #6a6a6a;
    --accent-orange: #f25a0f;
    --accent-blue: #2b6fc9;
    --panel-dark: #262626;
    --field-bg: #ffffff;
    --field-border: #cfcfcf;
    --field-text: #8a8a8a;
    --go-green: #6cc067;
    --btn-dark: #222222;
    --social-a: #3d5a98;
    --social-b: #1ea1e0;
    --social-c: #2a2a2a;
    --video-bg: #000000;
    --poster-top: #d9b08a;
    --poster-bottom: #8f847a;
    --control-bg: #1c1f20;
    --hd-blue: #1aa0e6;
  }
  * { box-sizing: border-box; margin: 0; padding: 0; }
  html, body { width: 1200px; height: 1000px; overflow: hidden; }
  body { position: relative; background: var(--page-bg); font-family: "Open Sans", Arial, sans-serif; }

  .site-header { position: absolute; left: 0; top: 0; width: 1200px; height: 57px; background: var(--header-bg); border-bottom: 1px solid var(--line); }
  .social { position: absolute; top: 15px; width: 28px; height: 28px; border-radius: 3px; }
  .social--one { left: 81px; background: var(--social-a); }
  .social--two { left: 117px; background: var(--social-b); }
  .social--three { left: 152px; background: var(--social-c); }

  .account-column { position: absolute; left: 738px; top: 58px; width: 405px; height: 942px; background: var(--side-bg); }

  .brand { position: absolute; left: 408px; top: 148px; width: 330px; height: 107px; background: #fff; display: flex; align-items: center; justify-content: center; gap: 10px; }
  .brand__mark { width: 22px; height: 22px; background: var(--accent-orange); border-radius: 3px; }
  .brand__name { font-size: 36px; font-weight: 700; color: #1f4aa0; letter-spacing: .5px; }

  .headline { position: absolute; right: 544px; top: 288px; font-size: 26px; font-weight: 400; color: var(--accent-orange); white-space: nowrap; }
  .tagline { position: absolute; right: 544px; top: 331px; font-family: Arial, sans-serif; font-size: 14px; font-weight: 700; color: var(--accent-blue); white-space: nowrap; }

  .video { position: absolute; left: 82px; top: 372px; width: 574px; height: 324px; background: var(--video-bg); }
  .video__poster { position: absolute; left: 15px; top: 15px; width: 542px; height: 248px; background: linear-gradient(180deg, var(--poster-top) 0%, var(--poster-bottom) 100%); }
  .video__big-play { position: absolute; left: 239px; top: 93px; }
  .video__controls { position: absolute; left: 0; top: 271px; width: 574px; height: 44px; }

  .intro { position: absolute; right: 544px; top: 730px; font-family: "Noticia Text", Georgia, serif; font-size: 13px; letter-spacing: .45px; line-height: 23.3px; color: var(--ink-body); text-align: right; white-space: nowrap; }
  .intro p + p { margin-top: 24px; }

  .section-title { position: absolute; left: 765px; width: 353px; font-size: 20px; font-weight: 400; color: var(--ink-soft); padding-bottom: 10px; border-bottom: 1px solid #bdbdbd; }
  .section-title--login { top: 85px; }
  .section-title--register { top: 487px; }

  .login-panel { position: absolute; left: 766px; top: 150px; width: 353px; height: 305px; background: var(--panel-dark); border-radius: 3px; padding: 26px 17px 0 21px; }
  .login-panel .field { height: 48px; border-radius: 3px; border: none; margin-bottom: 5px; padding-left: 21px; font-size: 12px; }
  .field { display: flex; align-items: center; width: 100%; background: var(--field-bg); border: 1px solid var(--field-border); color: var(--field-text); font-family: "Open Sans", Arial, sans-serif; }
  .check { display: flex; align-items: center; gap: 10px; font-size: 12px; color: #a8a8a8; }
  .check__box { width: 14px; height: 14px; border-radius: 2px; background: #6a6a6a; }
  .login-panel .check { margin-top: 20px; margin-left: 4px; }
  .btn { display: flex; align-items: center; justify-content: center; width: 100%; border-radius: 3px; color: #fff; font-weight: 600; font-size: 15px; }
  .btn--login { margin-top: 20px; height: 48px; background: var(--go-green); }
  .forgot { margin-top: 24px; margin-left: 3px; font-size: 12px; color: #a8a8a8; }

  .register-panel { position: absolute; left: 766px; top: 542px; width: 351px; height: 430px; background: #fff; padding: 18px 19px 0 17px; }
  .register-panel .field { height: 42px; margin-bottom: 5.2px; padding-left: 17px; font-size: 12px; border-radius: 2px; }
  .register-panel .check { margin-top: 18px; margin-left: 3px; font-size: 10.5px; color: #8a8a8a; }
  .register-panel .check__box { background: #f0f0f0; border: 1px solid #dcdcdc; width: 15px; height: 15px; }
  .btn--register { margin-top: 28px; height: 41px; background: var(--btn-dark); }
</style>
</head>
<body>
  <header class="site-header">
    <span class="social social--one" aria-label="Social profile"></span>
    <span class="social social--two" aria-label="Social profile"></span>
    <span class="social social--three" aria-label="Social profile"></span>
  </header>

  <aside class="account-column"></aside>

  <main>
    <div class="brand"><span class="brand__mark"></span><span class="brand__name">Nestwise</span></div>
    <h1 class="headline">The First Social Booking Network</h1>
    <p class="tagline">Nestwise is a new Social Booking Network</p>

    <div class="video">
      <div class="video__poster" role="img" aria-label="Video still: holiday guest relaxing at a seaside rental"></div>
      <svg class="video__big-play" width="88" height="88" viewBox="0 0 88 88" aria-hidden="true">
        <circle cx="44" cy="44" r="44" fill="rgba(255,255,255,.55)"/>
        <path d="M36 28 L60 44 L36 60 Z" fill="#333"/>
      </svg>
      <svg class="video__controls" width="574" height="44" viewBox="0 0 574 44" aria-hidden="true">
        <rect x="11" y="0" width="68" height="43" rx="3" fill="var(--control-bg)"/>
        <path d="M37 12 L53 21.5 L37 31 Z" fill="#fff"/>
        <rect x="88" y="9" width="476" height="32" rx="4" fill="var(--control-bg)"/>
        <rect x="98.5" y="19.5" width="345" height="11" fill="none" stroke="#8a8f91"/>
        <g fill="var(--hd-blue)">
          <rect x="453" y="19" width="2" height="12"/><rect x="457" y="19" width="2" height="12"/>
          <rect x="461" y="19" width="2" height="12"/><rect x="465" y="19" width="2" height="12"/>
          <rect x="469" y="19" width="2" height="12"/><rect x="473" y="19" width="2" height="12"/>
          <rect x="477" y="19" width="2" height="12"/><rect x="481" y="19" width="2" height="12"/>
          <rect x="485" y="19" width="2" height="12"/>
        </g>
        <text x="496" y="31" font-family="Arial, sans-serif" font-size="16" font-weight="700" font-style="italic" fill="var(--hd-blue)">HD</text>
        <g stroke="#fff" stroke-width="2" fill="none">
          <path d="M534 19 l4 4 M534 19 h4 M534 19 v4"/>
          <path d="M545 19 l-4 4 M545 19 h-4 M545 19 v4"/>
          <path d="M534 30 l4 -4 M534 30 h4 M534 30 v-4"/>
          <path d="M545 30 l-4 -4 M545 30 h-4 M545 30 v-4"/>
        </g>
      </svg>
    </div>

    <div class="intro">
      <p>Lorem Ipsum is simply dummy text of the printing and typesetting industry.<br>Lorem Ipsum has been the industry's standard dummy text ever since the<br>1500s, when an unknown printer took a galley of type and scrambled it to<br>make a type specimen book. It has survived not only five centuries</p>
      <p>But also the leap into electronic typesetting, remaining essentially unchanged.<br>It was popularised in the 1960s with the release of Leterline sheets containing<br>Lorem Ipsum passages, and more recently with desktop publishing software<br>like Pagecraft including versions of Lorem Ipsum.</p>
    </div>
  </main>

  <h2 class="section-title section-title--login">Login to your Account</h2>
  <form class="login-panel">
    <div class="field">User Name</div>
    <div class="field">Password</div>
    <div class="check"><span class="check__box"></span>Would you like us to remember you?</div>
    <div class="btn btn--login">Log Me In</div>
    <div class="forgot">I Forgot my Username / Password</div>
  </form>

  <h2 class="section-title section-title--register">Don’t have an account?</h2>
  <form class="register-panel">
    <div class="field">Full Name</div>
    <div class="field">User Name</div>
    <div class="field">Password</div>
    <div class="field">User Email Address</div>
    <div class="field">Set Your Contact Number</div>
    <div class="field">Whats your reason for joining</div>
    <div class="check"><span class="check__box"></span>I agree with the Nestwise terms &amp; condition</div>
    <div class="btn btn--register">Register Now</div>
  </form>
</body>
</html>
```